Land Buying Company Needs Letterhead for Direct Mail Marketing to Land Owners

We are looking for a professional letterhead that we will be including in our direct mail marketing. We will be sending this to land owners who may be interested in selling or purchasing land.

The letterhead needs to be editable. Headers and footers would look nice, but we are open. We would want it to include our address, website, phone, and email info. For right now the address to use for design purposes would the following:

Address: 415 Bramwell Avenue #600
Dallas, TX 75219
Website - www.quillridgeacres.example
Email - info@quillridgeacres.example
Phone - 866-402-ACRE

I have attached our logo zip file that we just had done on Pixel Guild. Let me know what questions you have, and thank you.

```html
<!DOCTYPE html>
<html lang="en">
<head>
<meta charset="utf-8">
<title>Quill Ridge Acres Letterhead</title>
<link rel="stylesheet" href="https://fonts.googleapis.com/css2?family=Open+Sans:wght@400;600&family=Roboto:wght@400&display=swap">
<style>
  :root {
    --backdrop: #e2e2e2;
    --paper: #ffffff;
    --forest: #44592a;
    --leaf: #8cc63f;
    --body-text: #8a8a8a;
    --contact-text: #3d3d3d;
    --signature-tone: #d9d9d9;
  }
  * { margin: 0; padding: 0; box-sizing: border-box; }
  html, body {
    width: 1200px; height: 800px; overflow: hidden;
    background: var(--backdrop);
  }
  .letterhead {
    position: absolute; left: 331px; top: 21px;
    width: 538px; height: 758px;
    background: var(--paper);
    font-family: "Open Sans", sans-serif;
  }
  .brand {
    position: absolute; left: 48px; top: 62px;
    display: flex; align-items: center; gap: 10px;
  }
  .brand-mark {
    width: 50px; height: 50px; border-radius: 50%;
    background: var(--forest);
  }
  .brand-name {
    font-family: "Open Sans", sans-serif;
    font-weight: 600; font-size: 22px; letter-spacing: 1px;
    color: var(--forest); text-transform: uppercase;
  }
  .letter-body {
    position: absolute; left: 48px; top: 175px; width: 441px;
    font-size: 9.9px; line-height: 14.6px; color: var(--body-text);
    text-align: justify;
  }
  .letter-body p { margin-bottom: 14.6px; }
  .signature {
    width: 64px; height: 60px; margin-top: 12px;
    background: var(--signature-tone); border-radius: 3px;
  }
  .contact {
    position: absolute; left: 48px; top: 690px;
    display: flex; gap: 10px; align-items: flex-end;
    font-family: "Roboto", sans-serif; font-size: 10.4px; line-height: 12.8px;
    color: var(--contact-text);
  }
  .contact-line { display: flex; align-items: center; gap: 3px; }
  .contact-line svg { width: 9px; height: 9px; flex: none; }
  .address { padding-bottom: 1px; }
  .base-band {
    position: absolute; left: 0; bottom: 0; width: 100%; height: 12px;
    background: var(--forest);
  }
</style>
</head>
<body>
  <main class="letterhead">
    <header class="brand">
      <div class="brand-mark"></div>
      <div class="brand-name">Quill Ridge Acres</div>
    </header>

    <section class="letter-body">
      <p>Dear customer,</p>
      <p>Lorem ipsum dolor sit amet, consectetur adipisicing elit, sed do eiusmod tempor incididunt ut labore et dolore magna aliqua. Ut enim ad minim veniam, quis nostrud exercitation ullamco laboris nisi ut aliquip ex ea commodo consequat. Duis aute irure dolor in reprehenderit in voluptate velit esse cillum dolore eu fugiat nulla pariatur. Excepteur sint occaecat cupidatat non proident, sunt in culpa qui officia deserunt mollit anim id est laborum.</p>
      <p>Lorem ipsum dolor sit amet, consectetur adipisicing elit, sed do eiusmod tempor incididunt ut labore et dolore magna aliqua. Ut enim ad minim veniam, quis nostrud exercitation ullamco laboris nisi ut aliquip ex ea commodo consequat. Duis aute irure dolor in reprehenderit in voluptate velit esse cillum dolore eu fugiat nulla pariatur. Excepteur sint occaecat cupidatat non proident, sunt in culpa qui officia deserunt mollit anim id est laborum.</p>
      <p>Lorem ipsum dolor sit amet, consectetur adipisicing elit, sed do eiusmod tempor incididunt ut labore et dolore magna aliqua. Ut enim ad minim veniam, quis nostrud exercitation ullamco laboris nisi ut aliquip ex ea commodo consequat. Duis aute irure dolor in reprehenderit in voluptate velit esse cillum dolore eu fugiat nulla pariatur. Excepteur sint occaecat cupidatat non proident, sunt in culpa qui officia deserunt mollit anim id est laborum.</p>
      <p>Lorem ipsum dolor sit amet, consectetur adipisicing elit, sed do eiusmod tempor incididunt ut labore et dolore magna aliqua. Ut enim ad minim veniam, quis nostrud exercitation ullamco laboris nisi ut aliquip ex ea commodo consequat. Duis aute irure dolor in reprehenderit.</p>
      <p>Yours Sincerely,</p>
      <div class="signature" role="img" aria-label="Handwritten signature"></div>
    </section>

    <footer class="contact">
      <div class="contact-details">
        <div class="contact-line">
          <svg viewBox="0 0 10 10" aria-hidden="true"><path fill="#8cc63f" d="M1 4c0-2 8-2 8 0v1H7V4H3v1H1zM2 6h6l1 3H1z"/></svg>
          <span>866-402-ACRE</span>
        </div>
        <div class="contact-line">
          <svg viewBox="0 0 10 10" aria-hidden="true"><rect x="0.5" y="2" width="9" height="6" fill="#8cc63f"/><path d="M0.5 2l4.5 3.5L9.5 2" fill="none" stroke="#fff" stroke-width="0.8"/></svg>
          <span>info@quillridgeacres.example</span>
        </div>
        <div class="contact-line">
          <svg viewBox="0 0 10 10" aria-hidden="true"><circle cx="5" cy="5" r="4.5" fill="#8cc63f"/><path d="M2 4c1 0 2 1 2 2s1 2 1 3M6 1c0 1 1 2 2 2" fill="none" stroke="#fff" stroke-width="0.8"/></svg>
          <span>www.quillridgeacres.example</span>
        </div>
      </div>
      <div class="address">
        <div>415 Bramwell Avenue #600</div>
        <div>Dallas, TX 75219</div>
      </div>
    </footer>

    <div class="base-band"></div>
  </main>
</body>
</html>
```